Design some Business Cards for "Keystone Driving School"

I need to have some artwork for business cards completed. The project is as follows:

PLEASE NOTE - THE BUSINESS CARDS MUST BE ON A "CAR BASED" THEME USING A NEW MODEL NISSAN PULSAR (if you show a vehicle on either side of the card).

Artwork must be forwarded in the following formats:

AI, ID, CDW or PSD
EPS, JPG, PDF and TIFF.

Must show the following detail:

Name: Glen Marwood
Postal address: PO Box 7159 Harbour Arcade Marlow Heights QLD 4871
Phone: 0427 913 604
Email: getonroad@keystonemotorlessons.com.au
Title: Driving instructor
Licence number: 81952
Words: "More than six years experience as a driving assessor"
Further words: "Learning is easy when you have the right teacher".

Card design is for both sides with the card itself to have rounded corners
Must incorporate the attached logos.

With the "L" logo, it can be different but needs to look like a learner drivers L plate.
The "WRMG" logo, the writing can be changed or moved on the card to be beside the logo etc

I'm not after a basic business card. I want something that looks stylish, professional and maybe incorporate a car photo etc.

Examples of similar ideas are noted on the following websites:

http://www.brindlecrestdrivingschool.com/
http://quillandpebblenotes.blogspot.com.au/2012/08/yet-more-webbybusiness-stuff.html
http://www.volterix.co.uk/personalised-stationary.html (The "prime, drive with Oliver business card")

There may be the opportunity to also complete the website for the business after this contest is completed.

Along with the winning entry I will be approaching one or two other designers with an offer to purchase their entry as well as I will eventually work with more than one business card.

Thank you for your time.

```html
<!DOCTYPE html>
<html lang="en">
<head>
<meta charset="utf-8">
<title>Keystone Driving School – Business Cards</title>
<link rel="stylesheet" href="https://fonts.googleapis.com/css2?family=PT+Sans:wght@400;700&family=Dancing+Script:wght@500&display=swap">
<style>
  :root {
    --page-bg: #e9e9e7;
    --brand-yellow: #f3e71e;
    --ink: #1b1b1b;
    --card-dark: #1f2224;
    --card-mid: #4a4d50;
    --card-light: #b9bcbf;
    --sky: #a9b6c0;
    --dash: #17191b;
    --white: #ffffff;
  }
  * { box-sizing: border-box; margin: 0; padding: 0; }
  html, body { width: 1200px; height: 800px; overflow: hidden; }
  body {
    background: var(--page-bg);
    font-family: "PT Sans", Arial, sans-serif;
    display: flex;
    align-items: center;
    justify-content: center;
    gap: 40px;
  }
  .card {
    position: relative;
    width: 540px;
    height: 330px;
    border-radius: 18px;
    overflow: hidden;
    box-shadow: 0 6px 18px rgba(0,0,0,0.18);
  }

  /* front */
  .card--front .photo-driver {
    position: absolute; inset: 0;
    background:
      radial-gradient(ellipse at 15% 20%, #cfd6dc 0%, transparent 55%),
      linear-gradient(160deg, var(--sky) 0%, #7d8890 35%, #3a3f43 60%, var(--dash) 85%);
  }

  /* back */
  .card--back {
    background: linear-gradient(120deg, var(--card-light) 0%, var(--card-mid) 45%, var(--card-dark) 100%);
  }
  .card--back .photo-driver-faint {
    position: absolute; left: 0; bottom: 0;
    width: 70%; height: 58%;
    background: linear-gradient(180deg, transparent 0%, rgba(40,44,48,0.35) 50%, rgba(30,32,35,0.55) 100%);
  }

  .tagline-tab {
    position: absolute; top: 0; right: 0;
    width: 68%; height: 42px;
    background: var(--brand-yellow);
    border-bottom-left-radius: 26px;
    display: flex; align-items: center;
    padding-left: 26px;
    font-family: "Dancing Script", cursive;
    font-size: 16px;
    color: var(--ink);
    white-space: nowrap;
  }

  .identity {
    position: absolute; top: 62px; left: 46%;
    color: var(--brand-yellow);
  }
  .identity__name {
    font-weight: 700; font-size: 36px; line-height: 1;
  }
  .identity__title {
    display: flex; align-items: center; gap: 10px;
    font-size: 27px; line-height: 1.2; margin-top: 2px;
  }
  .l-plate { flex: none; }

  .postal {
    position: absolute; top: 142px; right: 26px;
    text-align: right;
    color: var(--brand-yellow);
    font-size: 13px; line-height: 1.35;
    font-style: normal;
  }
  .contact {
    position: absolute; bottom: 28px; right: 26px;
    text-align: right;
    color: var(--brand-yellow);
    font-size: 13px; line-height: 1.4;
  }
  .contact b { font-weight: 700; }

  .partner-mark {
    position: absolute; left: 22px; bottom: 26px;
    display: flex; align-items: center; gap: 8px;
    color: var(--brand-yellow);
    font-size: 15px; font-weight: 700;
  }
  .partner-mark__dot {
    width: 30px; height: 30px; border-radius: 50%;
    background: var(--white);
  }
</style>
</head>
<body>

  <section class="card card--front">
    <div class="photo-driver" role="img" aria-label="Photo of a driver's hands on a steering wheel, dashboard and open road at dusk"></div>
    <div class="tagline-tab">“Learning is easy when you have the right teacher”</div>
    <div class="identity">
      <div class="identity__name">Glen Marwood</div>
      <div class="identity__title">
        <svg class="l-plate" width="26" height="26" viewBox="0 0 26 26" aria-hidden="true">
          <rect x="1" y="1" width="24" height="24" rx="2" fill="#f3e71e" stroke="#1b1b1b" stroke-width="1.5"/>
          <path d="M9 5 V20 H19 V16 H13 V5 Z" fill="#1b1b1b"/>
        </svg>
        Driving instructor
      </div>
    </div>
  </section>

  <section class="card card--back">
    <div class="photo-driver-faint" role="img" aria-label="Faded photo of a driver's hands on a steering wheel"></div>
    <div class="tagline-tab">More than six years experience as a driving assessor</div>
    <div class="identity">
      <div class="identity__name">Glen Marwood</div>
      <div class="identity__title">
        <svg class="l-plate" width="26" height="26" viewBox="0 0 26 26" aria-hidden="true">
          <rect x="1" y="1" width="24" height="24" rx="2" fill="#f3e71e" stroke="#1b1b1b" stroke-width="1.5"/>
          <path d="M9 5 V20 H19 V16 H13 V5 Z" fill="#1b1b1b"/>
        </svg>
        Driving instructor
      </div>
    </div>
    <address class="postal">
      PO Box 7159<br>Harbour Arcade Marlow Heights<br>QLD 4871
    </address>
    <div class="contact">
      <div><b>Phone:</b> 0427 913 604</div>
      <div><b>Email:</b> getonroad@keystonemotorlessons.com.au</div>
      <div>Instructor licence number: 81952</div>
    </div>
    <div class="partner-mark">
      <span class="partner-mark__dot"></span>WRMG
    </div>
  </section>

</body>
</html>
```